High end Electrical/home automation Business Card

Need a card for a high end electrical and home automation company utilising the existing logo.
Phone
Email
Website

Like black look with raised detail. Don’t necessarily need to keep colour of logo it could be made grayscale or white etc

Target Market(s)

High end clients

Contact Information for Business Card

Ridgeline Electrical

Requirements
Must have
• Logo, phone, email, website, address

High end look
Nice to have
• Black background card
Raised font
Should not have
• Lots of colour

```html
<!DOCTYPE html>
<html lang="en">
<head>
<meta charset="utf-8">
<title>Ridgeline Electrical – Business Card</title>
<link href="https://fonts.googleapis.com/css2?family=Arimo:wght@400;700&display=swap" rel="stylesheet">
<style>
  :root {
    --backdrop: #1a1a1a;
    --card: #212121;
    --card-edge: #2b2b2b;
    --blue: #2196d6;
    --white: #ffffff;
    --light: #e6e6e6;
  }
  * { box-sizing: border-box; margin: 0; padding: 0; }
  html, body { width: 1200px; height: 988px; overflow: hidden; }
  body {
    background: var(--backdrop);
    font-family: "Arimo", Arial, sans-serif;
    position: relative;
  }
  .card {
    position: absolute;
    width: 640px;
    height: 366px;
    background: var(--card);
    border-radius: 22px;
    border: 1px solid var(--card-edge);
    box-shadow: 0 18px 40px rgba(0,0,0,.55);
    overflow: hidden;
  }
  .card--front { left: 110px; top: 70px; }
  .card--back { left: 450px; top: 530px; }

  .brand {
    display: flex;
    align-items: center;
    gap: 14px;
    color: var(--white);
    font-weight: 700;
    letter-spacing: -0.5px;
  }
  .brand__mark {
    border-radius: 50%;
    background: var(--blue);
    flex: none;
  }
  .card--front .brand {
    position: absolute; left: 0; right: 0; top: 0; bottom: 0;
    justify-content: center;
    font-size: 46px;
  }
  .card--front .brand__mark { width: 40px; height: 40px; }

  .card--back .brand {
    position: absolute; left: 36px; top: 150px;
    font-size: 27px;
  }
  .card--back .brand__mark { width: 26px; height: 26px; }

  .divider {
    position: absolute;
    left: 318px; top: 46px;
    width: 1px; height: 200px;
    background: var(--blue);
  }
  .contact {
    position: absolute;
    left: 346px; top: 54px;
    color: var(--light);
  }
  .contact__name {
    color: var(--blue);
    font-weight: 700;
    font-size: 25px;
    letter-spacing: 0.3px;
  }
  .contact__title {
    font-size: 15px;
    margin-top: 2px;
    margin-bottom: 26px;
  }
  .contact__list { list-style: none; }
  .contact__item {
    display: flex; align-items: center; gap: 9px;
    font-size: 14px;
    margin-bottom: 9px;
  }
  .contact__item svg { width: 13px; height: 13px; fill: var(--blue); flex: none; }
  .accent { color: var(--blue); }

  .address-band {
    position: absolute;
    left: 0; right: 0; bottom: 26px;
    height: 40px;
    background: var(--blue);
    color: var(--white);
    font-size: 16px;
    display: flex; align-items: center; justify-content: center;
  }
</style>
</head>
<body>
  <section class="card card--front">
    <div class="brand"><span class="brand__mark"></span>Ridgeline Electrical</div>
  </section>

  <section class="card card--back">
    <div class="brand"><span class="brand__mark"></span>Ridgeline Electrical</div>
    <div class="divider"></div>
    <div class="contact">
      <p class="contact__name">DANIEL HARLOW</p>
      <p class="contact__title">Co-Founder</p>
      <ul class="contact__list">
        <li class="contact__item">
          <svg viewBox="0 0 24 24" aria-hidden="true"><path d="M6.6 10.8a15 15 0 0 0 6.6 6.6l2.2-2.2a1 1 0 0 1 1-.25 11.4 11.4 0 0 0 3.6.57 1 1 0 0 1 1 1V20a1 1 0 0 1-1 1A17 17 0 0 1 3 4a1 1 0 0 1 1-1h3.5a1 1 0 0 1 1 1c0 1.25.2 2.45.57 3.6a1 1 0 0 1-.25 1z"/></svg>
          123-555-0148
        </li>
        <li class="contact__item">
          <svg viewBox="0 0 24 24" aria-hidden="true"><path d="M2 5h20v14H2z M2 5l10 8 10-8" fill-rule="evenodd"/><path d="M3 6l9 7 9-7v1l-9 7-9-7z" fill="#212121"/></svg>
          daniel@ridgelineelectrical.com
        </li>
        <li class="contact__item">
          <svg viewBox="0 0 24 24" aria-hidden="true"><circle cx="12" cy="12" r="10"/><path d="M2 12h20M12 2c3 3 3 17 0 20M12 2c-3 3-3 17 0 20" stroke="#212121" stroke-width="1.5" fill="none"/></svg>
          www.<span class="accent">ridgelineelectrical</span>.com
        </li>
      </ul>
    </div>
    <div class="address-band">4820 Oakmont Ridge Rd Suite C Dayton.</div>
  </section>
</body>
</html>
```